Best in class business looking for best in class stationery that accurately reflects the brand image we are trying to build as the brand expands throughout the country. The Varying items should be an eye catching design that makes even the simplest letter or small business card stand out in the crowd.

Target Market(s)

Professionals

Industry/Entity Type

Real Estate

Other font styles liked:
• See atttached logo

Requirements
Must have
• Letterhead
• Business cards
• Envelopes
• Labels for larger mailings
Nice to have
• Folders
• Notebook
Should not have
• Stale design elements

```html
<!DOCTYPE html>
<html lang="en">
<head>
<meta charset="utf-8">
<title>Ridgeline Property Group – Business Cards</title>
<link href="https://fonts.googleapis.com/css2?family=Cinzel:wght@500&family=Open+Sans:wght@400;700&display=swap" rel="stylesheet">
<style>
  :root {
    --backdrop: #d6d6d6;
    --brand-blue: #2a3592;
    --brand-blue-light: #3d52b8;
    --brand-blue-dark: #1f2a78;
    --paper: #ffffff;
  }
  * { box-sizing: border-box; margin: 0; padding: 0; }
  html, body {
    width: 1200px; height: 800px; overflow: hidden;
    background: var(--backdrop);
  }
  .sheet {
    position: relative; width: 1200px; height: 800px;
    display: flex; align-items: center; justify-content: center; gap: 60px;
  }
  .card {
    position: relative; width: 510px; height: 292px; overflow: hidden;
    box-shadow: 0 6px 18px rgba(0,0,0,0.18);
  }
  .card-front {
    background: linear-gradient(120deg, var(--brand-blue-dark) 0%, var(--brand-blue-light) 45%, var(--brand-blue) 70%, var(--brand-blue-dark) 100%);
    display: flex; align-items: center; justify-content: center;
  }
  .wordmark { text-align: center; font-family: "Cinzel", serif; font-weight: 500; }
  .wordmark-name {
    display: flex; align-items: center; gap: 12px; justify-content: center;
    font-size: 30px; letter-spacing: 2px;
  }
  .wordmark-square { width: 16px; height: 16px; }
  .wordmark-rule { height: 1px; margin-top: 6px; }
  .card-front .wordmark { color: var(--paper); }
  .card-front .wordmark-square, .card-front .wordmark-rule { background: var(--paper); }

  .card-back { background: var(--paper); }
  .back-identity {
    position: absolute; top: 34px; left: 0; right: 0;
    display: flex; flex-direction: column; align-items: center;
  }
  .card-back .wordmark { color: var(--brand-blue); }
  .card-back .wordmark-name { font-size: 24px; }
  .card-back .wordmark-square, .card-back .wordmark-rule { background: var(--brand-blue); }
  .holder-name {
    margin-top: 14px; font-family: "Open Sans", sans-serif; font-weight: 700;
    font-size: 17px; color: var(--brand-blue);
  }
  .contact-band {
    position: absolute; left: 0; right: 0; top: 168px; height: 78px;
    background: linear-gradient(100deg, var(--brand-blue-dark), var(--brand-blue-light) 50%, var(--brand-blue));
    color: var(--paper); font-family: "Open Sans", sans-serif; font-size: 12.5px;
    display: flex; flex-direction: column; justify-content: center; align-items: center; gap: 8px;
  }
  .contact-line { display: flex; align-items: center; gap: 14px; }
  .contact-item { display: flex; align-items: center; gap: 5px; }
  .contact-item svg { width: 11px; height: 11px; }
  .base-strip {
    position: absolute; left: 0; right: 0; bottom: 18px; height: 6px;
    background: var(--brand-blue);
  }
</style>
</head>
<body>
<main class="sheet">
  <section class="card card-front">
    <div class="wordmark">
      <div class="wordmark-name"><span class="wordmark-square"></span>Ridgeline Property Group</div>
      <div class="wordmark-rule"></div>
    </div>
  </section>

  <section class="card card-back">
    <div class="back-identity">
      <div class="wordmark">
        <div class="wordmark-name"><span class="wordmark-square"></span>Ridgeline Property Group</div>
        <div class="wordmark-rule"></div>
      </div>
      <p class="holder-name">Example Name</p>
    </div>
    <div class="contact-band">
      <div class="contact-line">
        <span class="contact-item">
          <svg viewBox="0 0 12 12"><path d="M6 0.5a4 4 0 0 0-4 4c0 3 4 7 4 7s4-4 4-7a4 4 0 0 0-4-4z" fill="#fff"/><circle cx="6" cy="4.5" r="1.5" fill="#2a3592"/></svg>
          000 North Harbor Rd., Suite 200, Lakeview, US 0000
        </span>
      </div>
      <div class="contact-line">
        <span class="contact-item">
          <svg viewBox="0 0 12 12"><circle cx="6" cy="6" r="5.3" fill="none" stroke="#fff"/><path d="M4 3.5l1 0.2 0.4 1.4-0.7 0.6a4 4 0 0 0 1.6 1.6l0.6-0.7 1.4 0.4 0.2 1a1 1 0 0 1-1.1 0.8A5 5 0 0 1 3.2 4.6 1 1 0 0 1 4 3.5z" fill="#fff"/></svg>
          000.999.0000
        </span>
        <span class="contact-item">
          <svg viewBox="0 0 12 12"><rect x="1" y="2.5" width="10" height="7" fill="none" stroke="#fff"/><path d="M1 2.5l5 4 5-4" fill="none" stroke="#fff"/></svg>
          example@example.com
        </span>
        <span class="contact-item">
          <svg viewBox="0 0 12 12"><circle cx="6" cy="6" r="5.3" fill="none" stroke="#fff"/><path d="M0.7 6h10.6M6 0.7c-2.5 3-2.5 7.6 0 10.6M6 0.7c2.5 3 2.5 7.6 0 10.6" fill="none" stroke="#fff" stroke-width="0.8"/></svg>
          www.example.com
        </span>
      </div>
    </div>
    <div class="base-strip"></div>
  </section>
</main>
</body>
</html>
```